Brindle construction ltd staionary design
Project: Stationary
Stationary - Construction
Stationary
Professional
Directors Dan Brindle / Mark Brindle
BRINDLE CONSTRUCTION (GLOUCESTER) LTD
14 wexcombe road Gloucester GL4 8RQ
Brindleconstructionltd@fernmail.example
www.brindleconstructionlimited.example
would like stationary pack designed: business card, letterhead, envelope ect. Also a site sign please. Business card i would like black background to contrast my green logo with the logo in middle and details underneath. Letterhead i will leave to designer to come up with options. On site sign can i have logo ontop as main feature and underneath contact info with services incl ( New Builds, Extensions, Conversions, Refurbishments, Groundworks, Block Paving.) In logo attached use main logo ontop.
Main logo and underneath building contractor & Block paving specialist

```html
<!DOCTYPE html>
<html lang="en">
<head>
<meta charset="utf-8">
<title>Brindle Construction Ltd – Business Card</title>
<link href="https://fonts.googleapis.com/css2?family=Open+Sans:wght@400;600;700;800&display=swap" rel="stylesheet">
<style>
  :root {
    --backdrop: #a8863c;
    --card-white: #ffffff;
    --card-black: #0b0b0b;
    --brand-green: #3f9a2a;
    --ink: #3a3a3a;
    --ink-soft: #6b6b6b;
    --paper-text: #ffffff;
  }
  * { margin: 0; padding: 0; box-sizing: border-box; }
  html, body {
    width: 1200px; height: 686px; overflow: hidden;
    background: var(--backdrop);
    font-family: "Open Sans", Arial, sans-serif;
  }
  .stage { position: relative; width: 1200px; height: 686px; }

  .card {
    position: absolute;
    height: 396px;
    box-shadow: 0 6px 14px rgba(0,0,0,0.35);
  }

  /* Front (details) */
  .card-front { left: 60px; top: 140px; width: 540px; background: var(--card-white); }
  .directors {
    position: absolute; right: 34px; top: 34px;
    text-align: right; color: var(--brand-green);
    font-weight: 700; font-size: 16px; line-height: 20px;
  }
  .company-legal {
    position: absolute; right: 34px; top: 80px;
    font-size: 9.5px; line-height: 14px; font-weight: 600; color: var(--ink-soft);
    white-space: nowrap;
  }
  .divider {
    position: absolute; left: 0; right: 0; top: 117px;
    height: 3px; background: var(--brand-green);
  }
  .brand-front {
    position: absolute; left: 30px; top: 100px; height: 37px;
    background: var(--card-white); padding: 0 12px 0 6px;
    display: flex; align-items: center; gap: 8px;
    white-space: nowrap;
  }
  .brand-mark { width: 13px; height: 13px; background: var(--brand-green); flex: none; }
  .brand-name {
    font-weight: 800; font-size: 20px; line-height: 28px;
    color: var(--brand-green); letter-spacing: 0.4px;
  }
  .address {
    position: absolute; right: 34px; top: 150px;
    text-align: right; font-size: 13px; line-height: 19px; color: var(--ink);
  }
  .contact-list {
    position: absolute; right: 34px; top: 196px;
    list-style: none; text-align: right;
    font-size: 12.5px; line-height: 22px; color: var(--ink);
  }
  .contact-list li { display: flex; justify-content: flex-end; align-items: center; gap: 6px; white-space: nowrap; }
  .contact-icon { width: 13px; height: 13px; flex: none; }

  /* Back (logo) */
  .card-back { left: 607px; top: 283px; width: 550px; background: var(--card-black); }
  .brand-back {
    position: absolute; left: 0; right: 0; top: 128px;
    display: flex; justify-content: center; align-items: center; gap: 10px;
    white-space: nowrap;
  }
  .brand-back .brand-mark { width: 18px; height: 18px; background: var(--paper-text); }
  .brand-back .brand-name { color: var(--paper-text); font-size: 26px; line-height: 40px; letter-spacing: 0.6px; }
  .tagline {
    position: absolute; left: 0; right: 0; top: 208px;
    text-align: center; color: var(--paper-text);
    font-size: 12px; font-weight: 700;
  }
</style>
</head>
<body>
<main class="stage">

  <section class="card card-front">
    <div class="directors">
      <div>Directors Dan Brindle</div>
      <div>Mark Brindle</div>
    </div>
    <div class="company-legal">BRINDLE CONSTRUCTION (GLOUCESTER) LTD</div>
    <div class="divider"></div>
    <div class="brand-front">
      <span class="brand-mark"></span>
      <span class="brand-name">BRINDLE CONSTRUCTION LTD</span>
    </div>
    <div class="address">
      <div>14 wexcombe road</div>
      <div>Gloucester&nbsp; GL4 8RQ</div>
    </div>
    <ul class="contact-list">
      <li>01452 730264
        <svg class="contact-icon" viewBox="0 0 14 14"><path d="M3 1l2 0 1 3-1.5 1a7 7 0 0 0 4 4L10 7.5l3 1v2c0 1-1 2-2 2A10 10 0 0 1 1 3c0-1 1-2 2-2z" fill="var(--brand-green)"/></svg>
      </li>
      <li>07700 900418 / 07700 900592
        <svg class="contact-icon" viewBox="0 0 14 14"><rect x="3.5" y="0.5" width="7" height="13" rx="1.5" fill="var(--brand-green)"/><rect x="5" y="2" width="4" height="8" fill="#fff"/></svg>
      </li>
      <li>Brindleconstructionltd@fernmail.example
        <svg class="contact-icon" viewBox="0 0 14 14"><rect x="0.5" y="2.5" width="13" height="9" fill="var(--brand-green)"/><path d="M1 3l6 5 6-5" stroke="#fff" stroke-width="1.2" fill="none"/></svg>
      </li>
      <li>www.brindleconstructionlimited.example
        <svg class="contact-icon" viewBox="0 0 14 14"><circle cx="7" cy="7" r="6.5" fill="var(--brand-green)"/><path d="M1 7h12M7 1c-3 3-3 9 0 12M7 1c3 3 3 9 0 12" stroke="#fff" stroke-width="1" fill="none"/></svg>
      </li>
    </ul>
  </section>

  <section class="card card-back">
    <div class="brand-back">
      <span class="brand-mark"></span>
      <span class="brand-name">BRINDLE CONSTRUCTION LTD</span>
    </div>
    <p class="tagline">building contractor &amp; Block paving specialist</p>
  </section>

</main>
</body>
</html>
```